Bring me business with this creative business card

Design my new business card. I am looking for something different with an impact. People will take a look at this card & they will 1- see how different & creative I am, 2-understand what I do 3- Call me to meet me!

I make videos with a message, testimonials. I am dynamic, fun, creative & human. My new website is in construction but in the meantime you can check this old one: brightpath.ca & another one Ferncove.com & ferncove facebook page.
I make videos. sometimes with a cameraman, sometimes with my phone. As an ex Public Relations agent, the message is the most important thing for me. I want to make my clients shine! When they start with me they often remind me of a lamb, when I finish coaching them they are powerful like LIONS! That's why I need a powerful business card!

Target Market(s)

Entrepreneurs, solo entrepreneurs, small & medium companies & start ups. People i will meet while networking. People that need videos on their website & social Networks to get attention, to be visible. men & women. From 35 to 49 years old.
I am an ex Public relations agent. I used to send clients in traditional medias, now with videos they have more chances to be seen on google the new media. I do videos of the president, his team, his loyal clients saying how great the company is & expert videos like series so people can be seen for example every 1 st of every month with a short 2 minute video. Also with my 20 years in marketing & communications I can coach & give tips to anybody who needs it.
Target: anybody who would like my old website brightpath.ca & I also have another website but it will be off line soon: ferncove.com could give you ideas.

Industry/Entity Type

Communications

Contact Information for Business Card

I am in Montreal,So the business cards have to be the usual size like we have in Montreal: 9 cm x 5 cm
Details:My text: Martine Gaudreau Communication coach/Video lead. "Videos that tell your own story" off: 514-555-3047 cell: 514-555-6182. ferncove.com
martine@ferncove.com logo facebook, youtube, instagram

Colors
f37122

Requirements
Must have
• Dynamic, happy. Orange. Be creative in the look but NOT the shape of the card. Easy to read. Big enough to read.
Should not have
• No funny shapes: no round, no square, just the usual. I love creative but NOT on shape.

```html
<!DOCTYPE html>
<html lang="en">
<head>
<meta charset="utf-8">
<title>Ferncove business card</title>
<link href="https://fonts.googleapis.com/css2?family=Quicksand:wght@500;600&family=Kalam:wght@400&display=swap" rel="stylesheet">
<style>
  :root {
    --orange: #f37122;
    --ink: #1c1c1c;
    --card: #ffffff;
    --backdrop: #e9e9e9;
    --mark-warm: #f9b233;
  }
  * { box-sizing: border-box; margin: 0; padding: 0; }
  html, body { width: 1200px; height: 800px; overflow: hidden; }
  body {
    background: var(--backdrop);
    display: flex;
    align-items: center;
    justify-content: center;
    gap: 40px;
    font-family: "Quicksand", sans-serif;
  }
  .card {
    position: relative;
    width: 540px;
    height: 300px;
    background: var(--card);
    box-shadow: 0 6px 18px rgba(0,0,0,0.12);
    overflow: hidden;
  }
  .card--front { border-bottom: 5px solid var(--orange); }

  .brand {
    position: absolute;
    display: flex;
    flex-direction: column;
    align-items: center;
  }
  .card--front .brand { left: 50%; top: 50%; transform: translate(-50%, -50%); }
  .card--back .brand { left: 150px; top: 50%; transform: translate(-50%, -50%); }

  .brand__dot {
    width: 70px; height: 70px;
    border-radius: 50%;
    background: var(--mark-warm);
    margin-bottom: 14px;
  }
  .brand__name {
    font-family: "Quicksand", sans-serif;
    font-weight: 600;
    font-size: 34px;
    letter-spacing: 3px;
    color: var(--orange);
    text-transform: uppercase;
    line-height: 1;
  }

  .contact {
    position: absolute;
    left: 300px;
    top: 0;
    bottom: 0;
    width: 230px;
  }
  .contact__rule {
    position: absolute;
    left: 0;
    width: 4px;
    background: var(--orange);
  }
  .contact__rule--top { top: 0; height: 112px; }
  .contact__rule--bottom { top: 232px; height: 68px; }

  .contact__name {
    position: absolute;
    left: 14px;
    top: 36px;
    font-size: 30px;
    font-weight: 500;
    letter-spacing: 3px;
    color: var(--orange);
    line-height: 1;
  }
  .contact__role {
    position: absolute;
    left: 14px;
    top: 72px;
    font-size: 10.5px;
    font-weight: 600;
    color: var(--ink);
  }
  .contact__list {
    position: absolute;
    left: 14px;
    top: 98px;
    list-style: none;
    font-family: "Kalam", cursive;
    font-size: 16px;
    color: var(--ink);
    line-height: 1.45;
  }
  .contact__slogan { font-size: 15px; margin-bottom: 2px; white-space: nowrap; }
  .contact__item { display: flex; align-items: center; gap: 6px; white-space: nowrap; }
  .contact__icon { width: 12px; height: 12px; flex: none; }
</style>
</head>
<body>
  <section class="card card--front" aria-label="Card front">
    <div class="brand">
      <span class="brand__dot"></span>
      <span class="brand__name">Ferncove</span>
    </div>
  </section>

  <section class="card card--back" aria-label="Card back">
    <div class="brand">
      <span class="brand__dot"></span>
      <span class="brand__name">Ferncove</span>
    </div>

    <div class="contact">
      <span class="contact__rule contact__rule--top"></span>
      <span class="contact__rule contact__rule--bottom"></span>
      <h1 class="contact__name">Martine</h1>
      <p class="contact__role">Communication coach/Video lead</p>
      <ul class="contact__list">
        <li class="contact__slogan">Videos that tell your own story</li>
        <li class="contact__item">
          <svg class="contact__icon" viewBox="0 0 12 12" aria-hidden="true"><circle cx="6" cy="6" r="6" fill="#f37122"/><path d="M3.5 3.2c.4-.4.9-.3 1.1.1l.5.9c.2.3.1.6-.2.8l-.3.2c.4.8 1 1.4 1.8 1.8l.2-.3c.2-.3.5-.4.8-.2l.9.5c.4.2.5.7.1 1.1-.5.5-1.2.7-1.900.4C5 8 4 7 3.4 5.5c-.3-.8-.4-1.700.1-2.3z" fill="#fff"/></svg>
          514-555-3047
        </li>
        <li class="contact__item">
          <svg class="contact__icon" viewBox="0 0 12 12" aria-hidden="true"><circle cx="6" cy="6" r="6" fill="#f37122"/><rect x="4" y="2.5" width="4" height="7" rx="0.8" fill="#fff"/><rect x="4.6" y="3.3" width="2.8" height="4.6" fill="#f37122"/></svg>
          514-555-6182
        </li>
        <li class="contact__item">
          <svg class="contact__icon" viewBox="0 0 12 12" aria-hidden="true"><circle cx="6" cy="6" r="6" fill="#f37122"/><rect x="3" y="4" width="6" height="4" fill="#fff"/><path d="M3 4l3 2.2L9 4" stroke="#f37122" stroke-width="0.7" fill="none"/></svg>
          martine@ferncove.com
        </li>
        <li class="contact__item">
          <svg class="contact__icon" viewBox="0 0 12 12" aria-hidden="true"><circle cx="6" cy="6" r="6" fill="#f37122"/><circle cx="6" cy="6" r="3.2" stroke="#fff" stroke-width="0.7" fill="none"/><ellipse cx="6" cy="6" rx="1.3" ry="3.2" stroke="#fff" stroke-width="0.7" fill="none"/><path d="M2.8 6h6.4" stroke="#fff" stroke-width="0.7"/></svg>
          www.ferncove.com
        </li>
      </ul>
    </div>
  </section>
</body>
</html>
```